Tide Puffs. the aim is to sell vaping liquids based on mood or feelings

We are a company who sell vaping liquids. A designer from this site created a good logo for our company. I now need to use this logo and create a label to place onto vaping bottles. Unusually we will be selling vaping products based on Moods rather than flavours.

To be clear therefore the label should have our company Logo but then also reflect a particular type of Mood or feeling.

The designs for the various moods will then be printed as labels for our vaping bottles. We have 9 different Tide Puffs (see below) that we intend to bring to the market and general public

i would therfore like designs for the following 9 feelings/moods:

Love
Chilled
Happy
Energy
Desire
Bliss
Lust
Calm
High

the first attachment has our stand alone Logo.

i will then send some attachments of ideas we were playing around with to point you in the right direction. i will need the designs to be very colourful and to reflect the mood.

i do like the love hart one so it doesn't necessarily mean that we need to have images of people on the label. i will leave it to the designers to use images they feel best reflects the specific mood

Target Market(s)

General public

Industry/Entity Type

Retail

Colors

Designer to choose colors to be used in the design.

Requirements
Must have
• my company logo on any design
Nice to have
• vibrant colours or image to match the particular mood vape

```html
<!DOCTYPE html>
<html lang="en">
<head>
<meta charset="utf-8">
<title>Tide Puffs – Bottle Labels</title>
<link rel="stylesheet" href="https://fonts.googleapis.com/css2?family=Cinzel:wght@600&family=Montserrat:wght@600;700&family=Courgette&display=swap">
<style>
  :root {
    --canvas: #f3f3f3;
    --label-dark: #141414;
    --lust-deep: #3a0a0c;
    --lust-mid: #8e1419;
    --lust-bright: #e0323a;
    --calm-deep: #0f2a12;
    --calm-mid: #1f8a2c;
    --calm-bright: #49d65a;
    --love-deep: #2a0b22;
    --love-mid: #a3187c;
    --love-bright: #e83aaa;
    --ink-light: #ffffff;
  }
  * { box-sizing: border-box; margin: 0; padding: 0; }
  html, body { width: 1200px; height: 1200px; overflow: hidden; }
  body { background: var(--canvas); position: relative; font-family: "Montserrat", sans-serif; }

  .label {
    position: absolute;
    overflow: hidden;
    background: var(--label-dark);
  }
  .label-art { position: absolute; inset: 0; }
  .label--lust { left: 207px; top: 570px; width: 370px; height: 495px; }
  .label--calm { left: 808px; top: 293px; width: 170px; height: 230px; }
  .label--love { left: 808px; top: 860px; width: 180px; height: 245px; }

  .label--lust .label-art {
    background:
      radial-gradient(circle at 50% 45%, rgba(120,30,30,.6) 0 30%, transparent 55%),
      radial-gradient(ellipse at 20% 20%, var(--lust-bright) 0, transparent 40%),
      radial-gradient(ellipse at 85% 75%, var(--lust-bright) 0, transparent 35%),
      radial-gradient(ellipse at 70% 10%, var(--lust-mid) 0, transparent 45%),
      linear-gradient(160deg, var(--lust-mid), var(--lust-deep) 55%, var(--lust-mid));
  }
  .label--calm .label-art {
    background:
      radial-gradient(circle at 50% 40%, rgba(70,110,70,.6) 0 25%, transparent 55%),
      radial-gradient(ellipse at 15% 25%, var(--calm-bright) 0, transparent 40%),
      radial-gradient(ellipse at 85% 70%, var(--calm-bright) 0, transparent 38%),
      linear-gradient(160deg, var(--calm-mid), var(--calm-deep) 55%, var(--calm-mid));
  }
  .label--love .label-art {
    background:
      radial-gradient(circle at 50% 45%, rgba(120,60,100,.6) 0 25%, transparent 55%),
      radial-gradient(ellipse at 15% 20%, var(--love-bright) 0, transparent 40%),
      radial-gradient(ellipse at 85% 75%, var(--love-bright) 0, transparent 38%),
      linear-gradient(160deg, var(--love-mid), var(--love-deep) 55%, var(--love-mid));
  }

  .brand {
    position: absolute;
    left: 0; right: 0;
    display: flex; flex-direction: column; align-items: center; gap: 8px;
    color: var(--ink-light);
    font-weight: 700;
    text-align: center;
    line-height: 1;
  }
  .brand-dot { border: 2px solid var(--ink-light); border-radius: 50%; }
  .label--lust .brand { top: 170px; font-size: 44px; }
  .label--lust .brand-dot { width: 22px; height: 22px; }
  .label--calm .brand { top: 80px; font-size: 21px; gap: 5px; }
  .label--calm .brand-dot { width: 11px; height: 11px; border-width: 1.5px; }
  .label--love .brand { top: 86px; font-size: 22px; gap: 5px; }
  .label--love .brand-dot { width: 11px; height: 11px; border-width: 1.5px; }

  .feeling-band {
    position: absolute; left: 0; right: 0;
    display: flex; align-items: center; justify-content: center;
  }
  .feeling-band::before {
    content: ""; position: absolute; left: 0; right: 0; top: 50%;
    height: 3px; transform: translateY(-50%);
  }
  .feeling-name { position: relative; color: var(--ink-light); border-radius: 6px; line-height: 1; }

  .label--lust .feeling-band { top: 422px; }
  .label--lust .feeling-band::before { background: var(--lust-bright); height: 4px; }
  .label--lust .feeling-name {
    font-family: "Cinzel", serif; font-weight: 600; font-size: 30px;
    background: #b3161e; padding: 6px 16px 4px;
  }
  .label--calm .feeling-band { top: 194px; }
  .label--calm .feeling-band::before { background: var(--calm-bright); height: 2px; }
  .label--calm .feeling-name {
    font-weight: 700; font-size: 13px; letter-spacing: .5px;
    background: #2aa83a; padding: 3px 9px;
  }
  .label--love .feeling-band { top: 208px; }
  .label--love .feeling-band::before { background: var(--love-bright); height: 2px; }
  .label--love .feeling-name {
    font-family: "Courgette", cursive; font-size: 14px;
    background: #c21c86; padding: 3px 10px;
  }
</style>
</head>
<body>
  <section class="label label--lust" aria-label="Lust label">
    <div class="label-art" role="img" aria-label="Swirling red smoke texture"></div>
    <div class="brand"><span class="brand-dot"></span><span class="brand-name">Tide Puffs</span></div>
    <div class="feeling-band"><span class="feeling-name">LUST</span></div>
  </section>

  <section class="label label--calm" aria-label="Calm label">
    <div class="label-art" role="img" aria-label="Swirling green smoke texture"></div>
    <div class="brand"><span class="brand-dot"></span><span class="brand-name">Tide Puffs</span></div>
    <div class="feeling-band"><span class="feeling-name">CALM</span></div>
  </section>

  <section class="label label--love" aria-label="Love label">
    <div class="label-art" role="img" aria-label="Swirling pink smoke texture"></div>
    <div class="brand"><span class="brand-dot"></span><span class="brand-name">Tide Puffs</span></div>
    <div class="feeling-band"><span class="feeling-name">Love</span></div>
  </section>
</body>
</html>
```